Upmarket Artwork, Furniture Retailer needs to Improve existing Vendora Product Template Page

We need to improve an existing design for a Vendora product page. For professional quality we will then like to use the same designer for further work e.g vendora store(Web page)
We need a Web Designer for an exciting new online retailer based in Sydney. Our product is upmarket Scandanavian designed indoor furniture and Rattan outdoor furniture and Modernist Artwork.
Existing Banners,Logo, text, and template can be the same but the Graphic Design need improvement to give the Vendora product page an edge. We like the Green and Brown colours. Attached is teh logo and the extsing Product template

Reason: Thank you everyone for sending through your designs. Soem designs have come in late today and we need some extra time to contact designers. We will be in contact with you to let you know how you went. Kind Regards Delphine

Reason: Still waiting on some redesigns. My apologies for the belated reply. Thank you everyone for sending through great quality work.

Reason: My apologies for the delay. We are waiting on a re design to finalise. Thank you everyone for your patience. Cheers Delphine

Target Market(s)

Upmarket house proud 25-55 professionals

Industry/Entity Type

Graphic Design

Requirements
Must have
• To have an edge to Maximise Buyers
Nice to have
• To use the colours Greens and browns

```html
<!DOCTYPE html>
<html lang="en">
<head>
<meta charset="utf-8">
<title>Lumen House – Warranty</title>
<link rel="stylesheet" href="https://fonts.googleapis.com/css2?family=Oswald:wght@400&family=Open+Sans:wght@400;600&display=swap">
<style>
  :root{
    --green-bg:#5c9a1c;
    --green-dark:#4d8516;
    --green-head:#1f5a12;
    --brown:#6b2a12;
    --panel-top:#fafbee;
    --panel-bottom:#e6e7d0;
    --panel-border:#c6c8a2;
    --text:#222;
    --link:#1a3fb8;
    --white:#fff;
    --seal-red:#c8202a;
    --seal-soft:#e8c8c8;
  }
  *{box-sizing:border-box;margin:0;padding:0}
  html,body{width:1200px;height:1023px;overflow:hidden}
  body{background:var(--green-bg);position:relative;font-family:"Open Sans",Verdana,sans-serif;color:var(--text)}
  .page{position:absolute;left:34px;top:0;width:1098px;height:923px;background:var(--white)}
  .footer{position:absolute;left:0;top:923px;width:1200px;height:100px;background:var(--green-dark);border-top:2px solid #3e6d10}
  .footer p{position:absolute;top:28px;width:100%;text-align:center;font-family:Arial,sans-serif;font-size:11px;color:#1c2a08}

  .tabs{position:absolute;left:46px;top:17px;height:32px}
  .tab{position:absolute;top:0;height:32px;background:var(--brown);color:var(--white);font-size:13.5px;line-height:32px;text-align:center;border:1px solid #4a1c0a}
  .tab.active{background:var(--panel-top);color:#111;height:34px;border:1px solid var(--panel-border);border-bottom:none;z-index:2}

  .panel{position:absolute;left:28px;top:49px;width:1034px;height:362px;border:1px solid var(--panel-border);background:linear-gradient(var(--panel-top),var(--panel-bottom))}
  .section-title{font-family:"Oswald",sans-serif;font-weight:400;color:var(--green-head)}
  .panel .section-title{position:absolute;left:34px;top:24px;font-size:26px;line-height:1}
  .panel .rule{position:absolute;left:34px;top:69px;width:974px;border-top:1px dashed #6a6a5a}
  .panel .copy{position:absolute;left:34px;top:84px;width:690px;font-size:13.3px;line-height:21.5px;letter-spacing:-.1px}
  .panel .copy p+p{margin-top:21.5px}
  .panel .copy a{color:var(--link)}
  .seal{position:absolute;left:722px;top:90px;width:300px;height:222px;border-radius:50%;
    background:radial-gradient(ellipse at center,var(--seal-red) 0%,var(--seal-red) 45%,var(--seal-soft) 70%,rgba(232,200,200,0) 72%)}

  .featured .section-title{position:absolute;left:39px;top:459px;font-size:27px;line-height:1}
  .featured .rule{position:absolute;left:215px;top:485px;width:840px;border-top:2px dashed #9a9a8a}
  .card{position:absolute;top:527px;width:230px;height:337px;background:var(--white);box-shadow:0 0 5px rgba(0,0,0,.25)}
  .card .photo{position:absolute;left:19px;top:17px;width:194px;height:263px;background:linear-gradient(#5a3a12 0%,#8a5a20 25%,#2a3a5a 42%,#b88a4a 60%,#d8b880 100%)}
  .card .label{position:absolute;left:0;top:293px;width:230px;height:42px}
  .card .label span{position:absolute;inset:0;text-align:center;line-height:42px;color:var(--white);font-size:17.5px}
</style>
</head>
<body>
  <main class="page">
    <nav class="tabs">
      <div class="tab active" style="left:0;width:123px">Warranty</div>
      <div class="tab" style="left:124px;width:110px">Payment</div>
      <div class="tab" style="left:236px;width:104px">Delivery</div>
      <div class="tab" style="left:343px;width:105px">About Us</div>
    </nav>

    <section class="panel">
      <h1 class="section-title">Warranty</h1>
      <div class="rule"></div>
      <div class="copy">
        <p>Being a progressive retailer of design furniture, we are committed about delivering you quality products and attentive first class customer service.<br>
        For Further peace of mind all our products are supported by a 12 month comprehensive warranty whiuch can be extended.<br>
        We warrant all products for a period of 12 months under normal usage, to be free from defects in material and workmanship.</p>
        <p>Lumen House is so committed to the excelleance of our productsthat we offer&nbsp; a 30 day 100% money back guarantee. If you are not fully satisfied with your purchase, simply return the product back in its original packaging.<br>
        Contact us at <a href="#">admin@lumenhouse.com.au</a> if you require any assitance with your product after purchase.</p>
      </div>
      <div class="seal" role="img" aria-label="Satisfaction guarantee seal illustration"></div>
    </section>

    <section class="featured">
      <h2 class="section-title">Featured Products</h2>
      <div class="rule"></div>

      <article class="card" style="left:31px">
        <div class="photo" role="img" aria-label="Interior photo of a lounge with armchairs"></div>
        <svg class="label" viewBox="0 0 230 42"><polygon points="10,0 220,0 230,42 0,42" fill="var(--brown)"/></svg>
        <div class="label"><span>Indoor Furniture</span></div>
      </article>
      <article class="card" style="left:296px">
        <div class="photo" role="img" aria-label="Interior photo of a lounge with armchairs"></div>
        <svg class="label" viewBox="0 0 230 42"><polygon points="10,0 220,0 230,42 0,42" fill="var(--brown)"/></svg>
        <div class="label"><span>Outdoor Furniture</span></div>
      </article>
      <article class="card" style="left:560px">
        <div class="photo" role="img" aria-label="Interior photo of a lounge with armchairs"></div>
        <svg class="label" viewBox="0 0 230 42"><polygon points="10,0 220,0 230,42 0,42" fill="var(--brown)"/></svg>
        <div class="label"><span>Artwork</span></div>
      </article>
      <article class="card" style="left:825px">
        <div class="photo" role="img" aria-label="Interior photo of a lounge with armchairs"></div>
        <svg class="label" viewBox="0 0 230 42"><polygon points="10,0 220,0 230,42 0,42" fill="var(--brown)"/></svg>
        <div class="label"><span>Special</span></div>
      </article>
    </section>
  </main>

  <footer class="footer"><p>© 2012, All Rights Reserved</p></footer>
</body>
</html>
```